Perfect — here’s the updated version of your description with **title #1** and the integration/booking functionality references removed, while still keeping the “motivation to book” idea in the design style:
---
**Luxury Property Website Design – Dominican Republic**
We are looking to create a professional and visually appealing **website design** for a premium property that we will be promoting as a short-term rental.
The property is located in an **exclusive area of the Dominican Republic** and offers a high-end experience for guests. Our goal is to create a website that highlights the **luxury, comfort, and exclusivity** of the property, while motivating visitors to **make a reservation inquiry**.
**Key Requirements:**
* A clean, modern, and elegant design that reflects the **premium nature** of the property.
* High-quality visual presentation of the **property’s best features** (rooms, amenities, location, views, nearby attractions).
* Easy-to-navigate structure
* Mobile-friendly and optimized for all screen sizes.
* Space for testimonials or guest reviews to build trust.
**Design Style We Like:**
* Elegant and sophisticated, with a touch of tropical luxury.
* Use of high-quality photography, subtle animations, and a warm color palette that reflects the Caribbean atmosphere.
* A premium feel, similar to boutique hotel or luxury villa rental websites.
**Deliverables:**
* Homepage design.
* Property detail page design (with gallery, amenities, and booking inquiry section).
Contact page or About Us page
* Photo Gallery
The final design should capture the essence of a **luxury getaway** and make visitors feel compelled to reserve their night.

```html
<!DOCTYPE html>
<html lang="en">
<head>
<meta charset="utf-8">
<title>Contact – Costa Palmera Villa 43</title>
<link href="https://fonts.googleapis.com/css2?family=Roboto:wght@400;500;700&display=swap" rel="stylesheet">
<style>
:root{
  --orange:#d97706;
  --orange-dark:#b45309;
  --orange-soft:#fdefc4;
  --ink:#111827;
  --body:#4b5563;
  --muted:#6b7280;
  --line:#d1d5db;
  --page-soft:#f8f9fb;
  --facts-bg:#fefbea;
  --alert-bg:#fdf1f2;
  --alert:#b91c1c;
  --alert-dark:#991b1b;
  --footer:#121a2b;
  --white:#fff;
}
*{box-sizing:border-box;margin:0;padding:0}
html,body{width:1200px;height:2492px;overflow:hidden}
body{font-family:'Roboto',sans-serif;color:var(--ink);background:var(--white)}
svg{display:block}

/* header */
.site-header{position:absolute;top:0;left:0;width:1200px;height:56px;background:rgba(255,255,255,.93);display:flex;align-items:center;padding:0 28px;z-index:2;box-shadow:0 1px 3px rgba(0,0,0,.08)}
.brand{font-size:21px;font-weight:500;color:var(--orange)}
.main-nav{margin-left:auto;display:flex;gap:27px;align-items:center;font-size:14px;color:#374151}
.btn-book{background:var(--orange);color:#fff;font-size:12px;font-weight:500;padding:9px 13px;border-radius:4px;margin-left:0}

/* hero */
.hero{position:absolute;top:56px;left:0;width:1200px;height:456px;text-align:center;color:#fff}
.hero-photo{position:absolute;inset:0;background:radial-gradient(ellipse at 50% 30%,#c98a4a 0%,#7a4a2c 35%,#3c3a33 70%,#2a2c2a 100%)}
.hero-shade{position:absolute;inset:0;background:rgba(0,0,0,.15)}
.hero h1{position:relative;padding-top:136px;font-size:48px;font-weight:700}
.hero p{position:relative;margin:18px auto 0;width:690px;font-size:19px;line-height:27px;color:#f3f4f6}

/* contact info */
.contact-info{position:absolute;top:512px;left:0;width:1200px;height:513px;background:var(--page-soft);text-align:center}
.section-title{font-size:30px;font-weight:700;margin-top:54px}
.section-sub{font-size:16px;color:var(--body);margin-top:14px}
.info-cards{display:flex;gap:27px;justify-content:center;margin-top:40px}
.info-card{width:320px;height:296px;background:#fff;border-radius:10px;box-shadow:0 4px 14px rgba(0,0,0,.08);padding-top:27px}
.icon-badge{width:53px;height:53px;border-radius:50%;background:var(--orange-soft);display:flex;align-items:center;justify-content:center;margin:0 auto}
.info-card h3{font-size:17px;font-weight:500;margin-top:21px}
.info-card .lead{font-size:13.5px;color:var(--body);margin-top:16px}
.info-card .value{font-size:15px;color:var(--orange);margin-top:19px}
.info-card .value.dark{color:var(--ink);font-weight:500}
.info-card .note{font-size:11.5px;color:var(--muted);margin-top:10px}
.info-card .value + .note + .value{margin-top:12px}

/* form + aside */
.message-section{position:absolute;top:1025px;left:0;width:1200px;height:902px}
.form-col{position:absolute;left:94px;top:52px;width:486px}
.form-col h2{font-size:30px;font-weight:700}
.form-intro{font-size:16.5px;line-height:23px;color:var(--body);margin-top:18px}
.form-row{display:flex;gap:20px;margin-top:23px}
.field{flex:1}
.field label{display:block;font-size:11.5px;font-weight:500;color:#374151;margin-bottom:8px}
.input{height:38px;border:1px solid var(--line);border-radius:5px;font-size:11.5px;color:#9ca3af;padding:0 14px;display:flex;align-items:center;justify-content:space-between}
.input.filled{color:var(--ink)}
.textarea{height:105px;align-items:flex-start;padding:12px 14px;line-height:16px}
.count{font-size:9.5px;color:var(--muted);margin-top:5px}
.btn-send{margin-top:24px;height:50px;background:var(--orange);border-radius:7px;color:#fff;font-size:15px;font-weight:500;display:flex;align-items:center;justify-content:center;gap:8px}

.aside-col{position:absolute;left:620px;top:54px;width:486px}
.aside-col h3.loc{font-size:20px;font-weight:500}
.map{margin-top:12px;height:250px;background:#f3f4f6;border-radius:10px;box-shadow:0 3px 8px rgba(0,0,0,.06)}
.facts{margin-top:27px;background:var(--facts-bg);border-radius:10px;padding:27px 27px 26px}
.facts h3{font-size:20px;font-weight:500}
.fact{display:flex;gap:11px;margin-top:18px;align-items:center}
.fact:first-of-type{margin-top:23px}
.fact strong{display:block;font-size:13.5px;font-weight:500}
.fact span{display:block;font-size:11.5px;color:var(--body);margin-top:3px}
.emergency{margin-top:27px;background:var(--alert-bg);border-radius:10px;padding:27px 27px 28px}
.emergency h3{font-size:20px;font-weight:500;color:var(--alert-dark)}
.emergency p{font-size:13.5px;color:var(--alert);margin-top:14px}
.emergency-line{display:flex;gap:12px;align-items:center;margin-top:16px}
.emergency-line strong{display:block;font-size:15.5px;font-weight:500;color:var(--alert)}
.emergency-line span{display:block;font-size:11.5px;color:var(--alert);margin-top:4px}

/* cta */
.cta{position:absolute;top:1927px;left:0;width:1200px;height:263px;background:linear-gradient(110deg,#d97706 0%,#c2640d 60%,#b4520c 100%);text-align:center;color:#fff}
.cta h2{font-size:30px;font-weight:700;margin-top:52px}
.cta p{font-size:16.5px;margin-top:20px;color:#fde7c7}
.cta-actions{display:flex;gap:14px;justify-content:center;margin-top:28px}
.cta-btn{height:53px;border-radius:7px;display:flex;align-items:center;gap:9px;font-size:15px;font-weight:500;padding:0 27px}
.cta-btn.solid{background:#fff;color:var(--ink)}
.cta-btn.outline{border:2px solid #fff;color:#fff;padding:0 27px}

/* footer */
.site-footer{position:absolute;top:2190px;left:0;width:1200px;height:302px;background:var(--footer);color:#d1d5db}
.footer-brand{position:absolute;left:94px;top:44px;width:450px}
.footer-brand .brand{font-size:22px}
.footer-brand p{font-size:13.5px;line-height:22px;margin-top:14px}
.socials{display:flex;gap:14px;margin-top:15px}
.socials span{width:26px;height:26px;border-radius:50%;background:var(--orange)}
.footer-col{position:absolute;top:51px}
.footer-col h4{font-size:15px;font-weight:500;color:#fff}
.footer-col ul{list-style:none;margin-top:14px}
.footer-col li{font-size:13.5px;margin-bottom:10px}
.footer-contact li{display:flex;gap:8px;align-items:flex-start;line-height:20px;margin-bottom:7px}
.footer-contact svg{margin-top:5px}
.footer-bottom{position:absolute;left:94px;right:94px;top:213px;border-top:1px solid #273042;text-align:center;font-size:13px;color:#9ca3af;padding-top:37px}
</style>
</head>
<body>

<header class="site-header">
  <div class="brand">Costa Palmera</div>
  <nav class="main-nav">
    <span>Home</span><span>Property</span><span>Gallery</span><span>About</span><span>Contact</span>
    <span class="btn-book">Book Now</span>
  </nav>
</header>

<section class="hero">
  <div class="hero-photo" role="img" aria-label="Resort lobby with marble reception desk, wooden ceiling and tropical potted palms"></div>
  <div class="hero-shade"></div>
  <h1>Get In Touch</h1>
  <p>Ready to experience luxury? Our dedicated team is here to make your dream vacation a reality.</p>
</section>

<section class="contact-info">
  <h2 class="section-title">Contact Information</h2>
  <p class="section-sub">Multiple ways to reach our luxury concierge team</p>
  <div class="info-cards">
    <div class="info-card">
      <div class="icon-badge"><svg width="18" height="18" viewBox="0 0 24 24"><path fill="#d97706" d="M6.6 10.8a15 15 0 0 0 6.6 6.6l2.2-2.2c.3-.3.7-.4 1-.2 1.1.4 2.3.6 3.6.6.6 0 1 .4 1 1V20c0 .6-.4 1-1 1A17 17 0 0 1 3 4c0-.6.4-1 1-1h3.5c.6 0 1 .4 1 1 0 1.3.2 2.5.6 3.6.1.3 0 .7-.2 1z"/></svg></div>
      <h3>Phone</h3>
      <p class="lead">Available 24/7 for immediate assistance</p>
      <p class="value">+1 (809) 555-0181</p>
      <p class="note">Main Reservation Line</p>
      <p class="value">+1 (809) 555-0182</p>
      <p class="note">Concierge Services</p>
    </div>
    <div class="info-card">
      <div class="icon-badge"><svg width="18" height="18" viewBox="0 0 24 24"><rect x="3" y="5" width="18" height="14" rx="2" fill="#d97706"/><path d="M4 7l8 6 8-6" stroke="#fdefc4" stroke-width="1.8" fill="none"/></svg></div>
      <h3>Email</h3>
      <p class="lead">Detailed inquiries and special requests</p>
      <p class="value">reservations@costapalmera43.com</p>
      <p class="note">Bookings &amp; Availability</p>
      <p class="value">concierge@costapalmera43.com</p>
      <p class="note">Guest Services</p>
    </div>
    <div class="info-card">
      <div class="icon-badge"><svg width="18" height="18" viewBox="0 0 24 24"><path fill="#d97706" d="M12 2a7 7 0 0 0-7 7c0 5 7 13 7 13s7-8 7-13a7 7 0 0 0-7-7z"/><circle cx="12" cy="9" r="2.6" fill="#fdefc4"/></svg></div>
      <h3>Location</h3>
      <p class="lead">Exclusive Costa Palmera Resort</p>
      <p class="value dark">Costa Palmera Villa 43</p>
      <p class="note">La Romana, Dominican Republic</p>
      <p class="note">Private Villa Resort</p>
    </div>
  </div>
</section>

<section class="message-section">
  <div class="form-col">
    <h2>Send Us a Message</h2>
    <p class="form-intro">Fill out the form below and our team will get back to you within 2 hours during business hours.</p>
    <div class="form-row" style="margin-top:28px">
      <div class="field"><label>Full Name *</label><div class="input">Enter your full name</div></div>
      <div class="field"><label>Email Address *</label><div class="input">Enter your email</div></div>
    </div>
    <div class="form-row">
      <div class="field"><label>Phone Number</label><div class="input">Enter your phone number</div></div>
      <div class="field"><label>Subject</label><div class="input filled">Booking Inquiry <svg width="10" height="10" viewBox="0 0 10 10"><path d="M2 4l3 3 3-3" stroke="#6b7280" fill="none"/></svg></div></div>
    </div>
    <div class="form-row">
      <div class="field"><label>Check-In Date</label><div class="input filled">-/-/- <svg width="13" height="13" viewBox="0 0 14 14"><rect x="1.5" y="2.5" width="11" height="10" rx="1" stroke="#111827" stroke-width="1.4" fill="none"/><rect x="1.5" y="2.5" width="11" height="3" fill="#111827"/></svg></div></div>
      <div class="field"><label>Check-Out Date</label><div class="input filled">-/-/- <svg width="13" height="13" viewBox="0 0 14 14"><rect x="1.5" y="2.5" width="11" height="10" rx="1" stroke="#111827" stroke-width="1.4" fill="none"/><rect x="1.5" y="2.5" width="11" height="3" fill="#111827"/></svg></div></div>
      <div class="field"><label>Number of Guests</label><div class="input filled">1 Guest <svg width="10" height="10" viewBox="0 0 10 10"><path d="M2 4l3 3 3-3" stroke="#6b7280" fill="none"/></svg></div></div>
    </div>
    <div class="form-row">
      <div class="field"><label>Message *</label><div class="input textarea">Tell us about your requirements, special requests, or any questions you may have...</div><p class="count">0/500 characters</p></div>
    </div>
    <div class="btn-send"><svg width="14" height="14" viewBox="0 0 24 24"><path fill="#fff" d="M22 2L2 10l8 3 3 9z"/></svg>Send Message</div>
  </div>

  <aside class="aside-col">
    <h3 class="loc">Our Location</h3>
    <div class="map" role="img" aria-label="Map showing the villa location in La Romana"></div>
    <div class="facts">
      <h3>Quick Facts</h3>
      <div class="fact"><svg width="14" height="14" viewBox="0 0 24 24" fill="none" stroke="#d97706" stroke-width="2"><circle cx="12" cy="12" r="9"/><path d="M12 7v5l3 2"/></svg><div><strong>Response Time</strong><span>Within 2 hours during business hours</span></div></div>
      <div class="fact"><svg width="14" height="14" viewBox="0 0 24 24" fill="none" stroke="#d97706" stroke-width="2"><rect x="4" y="5" width="16" height="15" rx="2"/><path d="M4 10h16M8 3v4M16 3v4"/></svg><div><strong>Availability</strong><span>24/7 concierge support during stay</span></div></div>
      <div class="fact"><svg width="14" height="14" viewBox="0 0 24 24" fill="none" stroke="#d97706" stroke-width="2"><circle cx="12" cy="12" r="9"/><path d="M3 12h18M12 3c3 3 3 15 0 18M12 3c-3 3-3 15 0 18"/></svg><div><strong>Languages</strong><span>English, Spanish, French</span></div></div>
      <div class="fact"><svg width="14" height="14" viewBox="0 0 24 24" fill="none" stroke="#d97706" stroke-width="2"><path d="M12 3l7 3v6c0 4-3 7-7 9-4-2-7-5-7-9V6z"/><path d="M9 12l2 2 4-4"/></svg><div><strong>Booking Guarantee</strong><span>Secure reservations with instant confirmation</span></div></div>
    </div>
    <div class="emergency">
      <h3>Emergency Contact</h3>
      <p>For urgent matters during your stay:</p>
      <div class="emergency-line"><svg width="16" height="16" viewBox="0 0 24 24"><path fill="#b91c1c" d="M6.6 10.8a15 15 0 0 0 6.6 6.6l2.2-2.2c.3-.3.7-.4 1-.2 1.1.4 2.3.6 3.6.6.6 0 1 .4 1 1V20c0 .6-.4 1-1 1A17 17 0 0 1 3 4c0-.6.4-1 1-1h3.5c.6 0 1 .4 1 1 0 1.3.2 2.5.6 3.6.1.3 0 .7-.2 1z"/></svg><div><strong>+1 (809) 555-0190</strong><span>24/7 Emergency Line</span></div></div>
    </div>
  </aside>
</section>

<section class="cta">
  <h2>Ready to Experience Luxury?</h2>
  <p>Don't wait - our exclusive villa books quickly. Contact us today to secure your perfect dates.</p>
  <div class="cta-actions">
    <div class="cta-btn solid"><svg width="14" height="14" viewBox="0 0 24 24"><path fill="#111827" d="M6.6 10.8a15 15 0 0 0 6.6 6.6l2.2-2.2c.3-.3.7-.4 1-.2 1.1.4 2.3.6 3.6.6.6 0 1 .4 1 1V20c0 .6-.4 1-1 1A17 17 0 0 1 3 4c0-.6.4-1 1-1h3.5c.6 0 1 .4 1 1 0 1.3.2 2.5.6 3.6.1.3 0 .7-.2 1z"/></svg>Call Now</div>
    <div class="cta-btn outline"><svg width="14" height="14" viewBox="0 0 24 24" fill="none" stroke="#fff" stroke-width="2"><rect x="4" y="5" width="16" height="15" rx="2"/><path d="M4 10h16M8 3v4M16 3v4"/></svg>Check Availability</div>
  </div>
</section>

<footer class="site-footer">
  <div class="footer-brand">
    <div class="brand">Costa Palmera Villa 43</div>
    <p>Experience luxury and tranquility in one of the most exclusive areas of the Dominican Republic. Your perfect tropical getaway awaits with world-class amenities and breathtaking views.</p>
    <div class="socials"><span></span><span></span><span></span></div>
  </div>
  <div class="footer-col" style="left:613px">
    <h4>Quick Links</h4>
    <ul><li>Home</li><li>Property Details</li><li>Photo Gallery</li><li>About Us</li></ul>
  </div>
  <div class="footer-col footer-contact" style="left:873px">
    <h4>Contact</h4>
    <ul>
      <li><svg width="12" height="12" viewBox="0 0 24 24"><path fill="#d97706" d="M6.6 10.8a15 15 0 0 0 6.6 6.6l2.2-2.2c.3-.3.7-.4 1-.2 1.1.4 2.3.6 3.6.6.6 0 1 .4 1 1V20c0 .6-.4 1-1 1A17 17 0 0 1 3 4c0-.6.4-1 1-1h3.5c.6 0 1 .4 1 1 0 1.3.2 2.5.6 3.6.1.3 0 .7-.2 1z"/></svg>+1 (809) 555-0181</li>
      <li><svg width="12" height="12" viewBox="0 0 24 24" fill="none" stroke="#d97706" stroke-width="2"><rect x="3" y="5" width="18" height="14" rx="2"/><path d="M4 7l8 6 8-6"/></svg>info@costapalmera43.com</li>
      <li><svg width="12" height="12" viewBox="0 0 24 24" fill="none" stroke="#d97706" stroke-width="2"><path d="M12 2a7 7 0 0 0-7 7c0 5 7 13 7 13s7-8 7-13a7 7 0 0 0-7-7z"/><circle cx="12" cy="9" r="2.5"/></svg><span>Costa Palmera,<br>Dominican Republic</span></li>
    </ul>
  </div>
  <div class="footer-bottom">© 2024 Costa Palmera Villa 43. All rights reserved.</div>
</footer>

</body>
</html>
```